TRimélo label design

We need a new label design for 18.9 liter water bottles We attach examples of our brand logos and other bottle labels that we currently use. The new labels will carry our colorful brand (tRimélo) in the center, our contact telephone number (900417263) and information of the mantantial where they will be filled, (packaged by Murtana sl) along with its chemical composition, as seen in the old label design.

Font styles to use
Sans Serif

Colors

Designer to choose colors to be used in the design.

Requirements
Must have
• We need our type logo to be the protagonist of the design. It should include the text (bottled by MURTANA SL) with the smallest Toleburú logo in some area The ideal size of the label should be 450x120mm

```html
<!DOCTYPE html>
<html lang="es">
<head>
<meta charset="utf-8">
<title>tRimélo – etiqueta 18,9L</title>
<link rel="stylesheet" href="https://fonts.googleapis.com/css2?family=Open+Sans:wght@400;600;700;800&display=swap">
<style>
  :root {
    --blue: #229bd7;
    --blue-soft: #bcd8ef;
    --white: #ffffff;
    --purple: #4a2570;
    --bg: #ffffff;
  }
  * { margin: 0; padding: 0; box-sizing: border-box; }
  html, body { width: 1200px; height: 492px; overflow: hidden; background: var(--bg); }
  body { font-family: "Open Sans", Arial, sans-serif; color: var(--white); }
  .label { position: relative; width: 1200px; height: 492px; }
  .band { position: absolute; left: 0; width: 872px; background: var(--blue); }
  .band--top { top: 0; height: 28px; }
  .band--bottom { top: 469px; height: 27px; }
  .panel { position: absolute; top: 57px; height: 385px; }
  .panel--left { left: 0; width: 167px; background: var(--blue); text-align: center; }
  .panel--right { left: 707px; width: 165px; background: var(--blue); text-align: center; }
  .panel--center { left: 167px; width: 540px; overflow: hidden; }
  .backdrop { position: absolute; inset: 0;
    background: linear-gradient(135deg, #8fbde6 0%, #dbe9f6 35%, #ffffff 55%, #e3eef8 75%, #7fb3e2 100%); }
  .type-name { position: absolute; left: 20px; top: 29px; width: 130px; font-size: 12px; line-height: 14px; font-weight: 400; }
  .declared { position: absolute; left: 12px; top: 76px; width: 143px; font-size: 7.4px; line-height: 9px; text-transform: uppercase; }
  .care { position: absolute; left: 12px; top: 122px; width: 143px; font-size: 8.6px; line-height: 10px; text-transform: uppercase; font-weight: 600; }
  .composition { position: absolute; left: 22px; top: 230px; width: 122px; height: 91px; border: 1px solid var(--white); padding: 3px 4px; text-align: left; }
  .composition h3 { font-size: 6.6px; font-weight: 600; border-bottom: 1px solid var(--white); padding-bottom: 3px; margin-bottom: 3px; }
  .composition table { width: 100%; border-collapse: collapse; font-size: 5.8px; }
  .composition td { line-height: 8.5px; }
  .composition td:last-child { text-align: right; }
  .lab { position: absolute; left: 28px; top: 349px; width: 120px; font-size: 5px; line-height: 6.5px; text-align: left; font-weight: 600; text-transform: uppercase; }
  .batch-box { position: absolute; left: 20px; top: 318px; width: 125px; height: 55px; background: var(--white); }
  .brand { position: absolute; left: 60px; top: 225px; font-size: 108px; font-weight: 700; color: var(--purple); line-height: 1; letter-spacing: -2px; }
  .brand-dot { position: absolute; left: 360px; top: 60px; }
  .info { position: absolute; left: 6px; width: 153px; font-size: 7.6px; line-height: 10px; text-transform: uppercase; }
  .info--container { top: 43px; }
  .info--date { top: 128px; }
  .info--bottler { top: 185px; }
  .contact { position: absolute; left: 25px; top: 249px; width: 110px; height: 70px; border: 1.5px solid var(--white); border-radius: 8px; padding-top: 5px; }
  .contact-title { display: flex; align-items: flex-start; justify-content: center; gap: 3px; font-size: 9.5px; line-height: 11px; text-transform: uppercase; }
  .contact-title svg { margin-top: 10px; }
  .contact-line { border-top: 1px solid var(--white); width: 94px; margin: 2px auto 3px; }
  .contact-number { font-size: 15px; font-weight: 600; letter-spacing: 0.5px; }
  .product { position: absolute; left: 247px; top: 444px; font-size: 20px; font-weight: 700; letter-spacing: 5px; color: var(--blue); }
  .volume { position: absolute; left: 760px; top: 444px; font-size: 20px; font-weight: 700; letter-spacing: 1px; color: var(--blue); }
</style>
</head>
<body>
<div class="label">
  <div class="band band--top"></div>

  <section class="panel panel--left">
    <p class="type-name">Agua Mineral Natural de Mineralización débil.</p>
    <p class="declared">Declarada minero natural y de utilidad pública el 24 de julio de 2001.</p>
    <p class="care">Protegér de la luz solar. Preservar de olores agresivos. Conservar en lugar limpio, fresco y seco</p>
    <div class="composition">
      <h3>COMPOSICION QUIMICA (mg/L)</h3>
      <table>
        <tr><td>Residuo seco a 180°C</td><td>78</td></tr>
        <tr><td>Bicarbonatos (HCO₃)</td><td>12,8</td></tr>
        <tr><td>Sulfatos (SO₄)</td><td>11,5</td></tr>
        <tr><td>Cloruros (Cl)</td><td>12,9</td></tr>
        <tr><td>Calcio (Ca)</td><td>7,8</td></tr>
        <tr><td>Magnesio (Mg)</td><td>1,6</td></tr>
        <tr><td>Sodio (Na)</td><td>10,5</td></tr>
        <tr><td>Silice (SiO₂)</td><td>7,3</td></tr>
      </table>
    </div>
    <p class="lab">Composicion analitica en mg/l.<br>Laboratorio Dr. Alen Casto - 2018</p>
    <div class="batch-box" style="top:375px"></div>
  </section>

  <section class="panel panel--center">
    <div class="backdrop" role="img" aria-label="Fondo degradado azul y blanco con gotas de agua"></div>
    <svg class="brand-dot" width="110" height="110" viewBox="0 0 110 110" aria-hidden="true">
      <circle cx="55" cy="55" r="52" fill="var(--blue)"/>
    </svg>
    <div class="brand">tRimélo</div>
  </section>

  <section class="panel panel--right">
    <p class="info info--container">Envase retornable<br>de policarbonato sometido<br>a rigurosos sistemas<br>de higienización</p>
    <p class="info info--date">Consumir preferentemente<br>antes del - lote: ver el tapón</p>
    <p class="info info--bottler">Embotellado por:<br>MURTANA, S.L.<br>Pedreira - Vilanova de Salcedo<br>N.º RS. 31862/PO</p>
    <div class="contact">
      <div class="contact-title">
        <svg width="9" height="11" viewBox="0 0 24 24" aria-hidden="true"><path fill="#fff" d="M6.6 10.8a15 15 0 0 0 6.6 6.6l2.2-2.2a1 1 0 0 1 1-.25 11.4 11.4 0 0 0 3.6.57 1 1 0 0 1 1 1V20a1 1 0 0 1-1 1A17 17 0 0 1 3 4a1 1 0 0 1 1-1h3.5a1 1 0 0 1 1 1c0 1.25.2 2.45.57 3.57a1 1 0 0 1-.25 1z"/></svg>
        <span>Número telefónico<br>de contacto</span>
      </div>
      <div class="contact-line"></div>
      <div class="contact-number">900417263</div>
    </div>
  </section>

  <div class="product">AGUA MINERAL NATURAL</div>
  <div class="volume">18,9L</div>

  <div class="band band--bottom"></div>
</div>
</body>
</html>
```